Criação de Cartao de Visita para Consultoria de Negócios
A empresa queria:
" CONSULTORIA PARA EMPRESAS E GRUPOS FAMILIARES PARA REESTRUTURAÇÃO FINANCEIRA E DE NEGÓCIOS "

```html
<!DOCTYPE html>
<html lang="pt-BR">
<head>
<meta charset="UTF-8">
<title>Norte consulting – Cartão de visita</title>
<link href="https://fonts.googleapis.com/css2?family=Roboto:wght@400;500;700&family=Roboto+Slab:wght@400&display=swap" rel="stylesheet">
<style>
  :root {
    --teal-deep: #0b4a4d;
    --teal: #12585a;
    --teal-light: #1d6b6c;
    --paper: #f4f5f5;
    --paper-shade: #e7eaea;
    --ink: #1f2a2b;
    --muted: #5d6566;
    --stage: #eef0f0;
    --white: #ffffff;
  }
  * { margin: 0; padding: 0; box-sizing: border-box; }
  html, body { width: 1200px; height: 1200px; overflow: hidden; }
  body { background: var(--stage); font-family: "Roboto", Arial, sans-serif; position: relative; }

  .card {
    position: absolute;
    left: 235px;
    width: 734px;
    height: 408px;
    overflow: hidden;
  }

  /* Front */
  .card-front { top: 160px; background: var(--teal); }
  .front-backdrop { position: absolute; inset: 0; width: 100%; height: 100%; }
  .front-brand {
    position: absolute;
    left: 0; right: 0; top: 0; bottom: 0;
    display: flex; align-items: center; justify-content: center;
    gap: 18px;
  }
  .brand-dot { width: 26px; height: 26px; border-radius: 50%; background: var(--white); }
  .brand-name {
    font-family: "Roboto Slab", Georgia, serif;
    font-weight: 400;
    color: var(--white);
    font-size: 44px;
    letter-spacing: 0.5px;
  }

  /* Back */
  .card-back { top: 640px; background: linear-gradient(180deg, var(--white), var(--paper)); }
  .back-decor { position: absolute; left: 90px; top: 10px; width: 230px; height: 360px; }
  .back-brand {
    position: absolute; left: 440px; top: 80px;
    display: flex; align-items: center; gap: 10px;
  }
  .back-brand .brand-dot { width: 14px; height: 14px; background: var(--teal); }
  .back-brand .brand-name { color: var(--teal); font-size: 26px; }
  .holder { position: absolute; left: 440px; top: 202px; width: 200px; text-align: center; }
  .holder-name { font-size: 15px; font-weight: 700; color: var(--ink); }
  .holder-role { font-size: 10px; color: var(--muted); margin-top: 6px; letter-spacing: 0.5px; }

  .contact { position: absolute; left: 52px; top: 250px; color: var(--ink); }
  .contact-web, .contact-phone { font-size: 17px; }
  .contact-phone { margin-top: 10px; }
  .contact-address { font-size: 14px; line-height: 19px; margin-top: 16px; }

  .side-bar { position: absolute; left: 0; top: 230px; width: 10px; height: 130px; background: var(--teal); }
  .base-line { position: absolute; left: 0; right: 0; bottom: 8px; height: 2px; background: var(--teal-light); opacity: 0.5; }
  .base-band { position: absolute; right: 0; bottom: 0; width: 290px; height: 14px; background: var(--teal); }
</style>
</head>
<body>
  <section class="card card-front" aria-label="Frente do cartão">
    <svg class="front-backdrop" role="img" aria-label="Fotografia esmaecida de equipamentos de escritório e telas em tons de verde-petróleo" viewBox="0 0 734 408" preserveAspectRatio="none">
      <defs>
        <radialGradient id="frontGlow" cx="62%" cy="40%" r="60%">
          <stop offset="0" stop-color="#1f6f70"/>
          <stop offset="1" stop-color="#12585a"/>
        </radialGradient>
      </defs>
      <rect width="734" height="408" fill="url(#frontGlow)"/>
    </svg>
    <div class="front-brand">
      <span class="brand-dot"></span>
      <span class="brand-name">Norte consulting</span>
    </div>
  </section>

  <section class="card card-back" aria-label="Verso do cartão">
    <svg class="back-decor" role="img" aria-label="Marca-d'água clara da empresa" viewBox="0 0 230 360">
      <rect width="230" height="360" rx="20" fill="#e9ecec" opacity="0.6"/>
    </svg>
    <div class="back-brand">
      <span class="brand-dot"></span>
      <span class="brand-name">Norte consulting</span>
    </div>
    <div class="holder">
      <p class="holder-name">Nome Sobrenome</p>
      <p class="holder-role">FUNÇÃO</p>
    </div>
    <div class="contact">
      <p class="contact-web">www.norteconsulting.com.br</p>
      <p class="contact-phone">+ 55 67 3400-1875</p>
      <p class="contact-address">Av. das Palmeiras, 2.410 - 9º andar - Sala 902<br>Vila Serena - MS - CEP 79000-100</p>
    </div>
    <span class="side-bar"></span>
    <span class="base-line"></span>
    <span class="base-band"></span>
  </section>
</body>
</html>
```